Visitenkarten- und Briefpapier Design - Logo vorhanden!
Zielgruppe
Wir sind eine Projektentwicklungs GmbH die Grundstücke kauft, projektiert und wieder verkauft. Eine zukünftige GmbH ist für den Innenausbau von neuen Häusern (EFH,DHH,MFH) gedacht. Wir sind ebenfalls für den Vertrieb von Häusern tätig.
Unsere Zielgruppe sind Endkunden im Immobilienbereich die Grundstücke und/oder Häuser bis Schlüsselfertig kaufen möchten, sowie Grundstückseigentümer die verkaufen wollen.
Wir benötigen Visitenkarten UND Briefpapier.
Aufgabenstellung
Bitte vorhandenes Logo verwenden.
Briefpapier:
Es soll ein ansprechendes modernes Design sein. Wir lassen uns gerne überraschen und versuchen schnellstmöglich Feedback zu geben.
Visitenkarte:
Es soll ein ansprechendes modernes Design sein. Die Visitenkarte bitte mit 2 Seiten, auf der Rückseite könnten wir uns das Dunkle ZERANT Logo sehr gut vorstellen (nur Logo).

```html
<!DOCTYPE html>
<html lang="de">
<head>
<meta charset="utf-8">
<title>ZERANT – Briefpapier und Visitenkarten</title>
<link rel="stylesheet" href="https://fonts.googleapis.com/css2?family=EB+Garamond:wght@400;500;700&display=swap">
<style>
  :root {
    --navy: #1e202b;
    --paper: #ffffff;
    --ink: #1e202b;
    --shadow: rgba(0, 0, 0, 0.38);
  }
  * { margin: 0; padding: 0; box-sizing: border-box; }
  html, body { width: 849px; height: 1200px; overflow: hidden; background: var(--paper); }
  body { font-family: "EB Garamond", Garamond, serif; color: var(--ink); }
  .sheet { position: relative; width: 849px; height: 1200px; overflow: hidden; background: var(--paper); }
  .sheet-frame { position: absolute; left: 0; top: 0; width: 849px; height: 1200px; }

  .brand-name {
    position: absolute; left: 57px; top: 130px;
    font-size: 52px; font-weight: 400; letter-spacing: 1px; line-height: 1;
    color: var(--ink);
  }

  .sender { position: absolute; left: 595px; top: 60px; font-size: 10.6px; line-height: 13.6px; }
  .sender-name { font-size: 18px; font-weight: 700; line-height: 20px; letter-spacing: 0.3px; }
  .sender-tagline { margin-bottom: 12px; }
  .sender-row { display: flex; }
  .sender-row .label { width: 61px; }
  .sender-block { margin-bottom: 13px; }

  .footer-col { position: absolute; top: 1098px; font-size: 10.8px; line-height: 13.6px; text-transform: uppercase; }
  .footer-company { left: 119px; }
  .footer-bank { left: 501px; }

  .card { position: absolute; top: 317px; width: 226px; height: 388px; overflow: hidden; box-shadow: 7px 10px 12px var(--shadow); }
  .card-front { left: 294px; background: var(--paper); }
  .card-back { left: 577px; background: var(--navy); }
  .card-front-shape { position: absolute; left: 0; top: 0; width: 226px; height: 388px; }

  .card-mark { position: absolute; color: var(--paper); font-weight: 400; white-space: nowrap; transform-origin: left top; line-height: 1; }
  .card-front .card-mark { left: 20px; top: 22px; font-size: 17px; transform: rotate(26deg); letter-spacing: 0.5px; }
  .card-back .card-mark { left: 32px; top: 118px; font-size: 40px; transform: rotate(26deg); letter-spacing: 1px; }

  .card-details { position: absolute; left: 90px; top: 106px; transform: rotate(26.4deg); transform-origin: left top; white-space: nowrap; }
  .holder-name { font-size: 18px; font-weight: 700; line-height: 19px; }
  .holder-role { font-size: 10px; line-height: 12px; }
  .card-contact { margin-top: 30px; font-size: 9.6px; line-height: 12.5px; }
  .card-contact .row { display: flex; }
  .card-contact .label { width: 62px; }
</style>
</head>
<body>
<div class="sheet">
  <svg class="sheet-frame" viewBox="0 0 849 1200" aria-hidden="true">
    <polygon fill="var(--navy)" points="2,0 421,0 440,40 2,40"/>
    <polygon fill="var(--navy)" points="455,0 708,0 727,40 573,40 573,236"/>
    <polygon fill="var(--navy)" points="738,0 849,0 849,40 758,40"/>
    <polygon fill="var(--navy)" points="320,1098 320,1182 363,1182"/>
    <polygon fill="var(--navy)" points="677,1098 677,1182 720,1182"/>
    <rect fill="var(--navy)" x="0" y="1182" width="849" height="18"/>
  </svg>

  <div class="brand-name">ZERANT</div>

  <div class="sender">
    <div class="sender-name">ZERANT</div>
    <div class="sender-tagline">Imobilienverwaltung</div>
    <div class="sender-block">
      <div>Musterstraße&nbsp; 123</div>
      <div>Musterstadt&nbsp;&nbsp; 12345</div>
    </div>
    <div class="sender-block">
      <div class="sender-row"><span class="label">Telefon:</span><span>+49 (0) 123 456789</span></div>
      <div class="sender-row"><span class="label">Email:</span><span>info@zerant.com</span></div>
      <div class="sender-row"><span class="label">Web:</span><span>www.zerant.com</span></div>
    </div>
    <div class="sender-row"><span class="label">Steuernr.:</span><span>123/456/789</span></div>
  </div>

  <div class="card card-front">
    <svg class="card-front-shape" viewBox="0 0 226 388" aria-hidden="true">
      <rect fill="var(--navy)" width="226" height="388"/>
      <polygon fill="var(--paper)" points="88,89 226,157 226,388 0,388 0,264"/>
    </svg>
    <div class="card-mark">ZERANT</div>
    <div class="card-details">
      <div class="holder-name">Max<br>Mustermann</div>
      <div class="holder-role">Musterposition</div>
      <div class="card-contact">
        <div class="row"><span class="label">Telefon:</span><span>+49 (0) 123 456789</span></div>
        <div class="row"><span class="label">Email:</span><span>m.mustermann@zerant.com</span></div>
        <div class="row"><span class="label">Web:</span><span>www.zerant.com</span></div>
      </div>
    </div>
  </div>

  <div class="card card-back">
    <div class="card-mark">ZERANT</div>
  </div>

  <div class="footer-col footer-company">
    <div>Mustertext</div>
    <div>Firmenname</div>
    <div>Geschäftsführung M. Muster</div>
    <div>Firmen Steuernummer</div>
    <div>Firmen Ust-ID-Nr</div>
  </div>
  <div class="footer-col footer-bank">
    <div>Musterbankverbindung 1</div>
    <div>BLZ 123 456 78</div>
    <div>Konto-Nr. 1 234 567</div>
    <div>IBAN 123 456 789 123 456 789</div>
    <div>BIC Muster</div>
  </div>
</div>
</body>
</html>
```